High-end residential home builder needs a business card design

We need a new business card design for a small residential construction company based in Boise, Idaho. We specialize in building custom high-end homes and remodels, with a focus on great design and craftsmanship.

We would like to use our current logo, but open to new color suggestions.
Just looking for a clean, sharp, modern design that looks high-end.

Target Market(s)

Upscale clientele

Industry/Entity Type

Contractor

Contact Information for Business Card

Company: Stonefield Custom Builders
Name: Marcus Tilley
Phone number: 208 367 4120
Email: MarcusTilleySCB@mailbox-example.com
Website: Stonefieldcustombuilders-example.com

Font styles to use
Serif
Sans Serif

Requirements
Must have
• Company Logo
Company name
My name
My phone number
My email
Company website
Nice to have
• I have attached a few photos of cards that I really like.

```html
<!DOCTYPE html>
<html lang="en">
<head>
<meta charset="utf-8">
<title>Stonefield Custom Builders – Business Card</title>
<link href="https://fonts.googleapis.com/css2?family=Josefin+Sans:wght@400;600&display=swap" rel="stylesheet">
<style>
  :root {
    --page-bg: #e7e8eb;
    --card-white: #f1f1f3;
    --accent-orange: #d98a2b;
    --ink-brown: #2b1a0f;
    --back-brown: #2f1d0e;
    --back-brown-light: #3a250f;
    --mark-white: #f4f1ec;
  }
  * { margin: 0; padding: 0; box-sizing: border-box; }
  html, body {
    width: 1200px; height: 1200px; overflow: hidden;
    background: var(--page-bg);
    font-family: "Josefin Sans", sans-serif;
  }
  .canvas { position: relative; width: 1200px; height: 1200px; }

  .card { position: absolute; left: 227px; width: 746px; height: 425px; }
  .card-front { top: 135px; background: var(--card-white); }
  .card-back {
    top: 639px;
    background: linear-gradient(100deg, var(--back-brown) 0%, var(--back-brown) 55%, var(--back-brown-light) 100%);
  }

  .company-block {
    position: absolute; left: 28px; top: 300px; transform: translateY(-50%);
    top: 193px;
    display: flex; align-items: center; gap: 14px;
  }
  .company-dot {
    width: 70px; height: 70px; border-radius: 50%;
    border: 2px solid var(--ink-brown); flex: none;
  }
  .company-name {
    color: var(--ink-brown); font-weight: 600;
    font-size: 19px; letter-spacing: 4px; text-transform: uppercase;
    line-height: 1.35;
  }

  .person { position: absolute; left: 403px; top: 120px; }
  .person-name {
    color: var(--accent-orange); font-weight: 400;
    font-size: 26px; letter-spacing: 1px; text-transform: uppercase;
  }
  .person-title { color: var(--ink-brown); font-size: 19px; margin-top: 4px; letter-spacing: 0.5px; }

  .divider {
    position: absolute; left: 403px; right: 0; top: 202px;
    height: 1.5px; background: var(--ink-brown);
  }

  .contact-list { position: absolute; left: 403px; top: 236px; list-style: none; }
  .contact-item {
    display: flex; align-items: center; gap: 14px;
    height: 25.5px; color: var(--ink-brown); font-size: 16.5px; letter-spacing: 0.3px;
  }
  .contact-icon { width: 17px; height: 17px; flex: none; }

  .back-surface { position: absolute; inset: 0; }
  .back-name {
    position: absolute; left: 863px; top: 299px; transform: translateX(-50%);
    left: 611px;
    color: var(--mark-white); font-size: 10px; font-weight: 600;
    letter-spacing: 2px; text-transform: uppercase; white-space: nowrap;
  }
</style>
</head>
<body>
<main class="canvas">

  <section class="card card-front">
    <div class="company-block">
      <span class="company-dot"></span>
      <div class="company-name">Stonefield<br>Custom Builders</div>
    </div>

    <div class="person">
      <h1 class="person-name">Marcus Tilley</h1>
      <p class="person-title">Owner and operator</p>
    </div>

    <div class="divider"></div>

    <ul class="contact-list">
      <li class="contact-item">
        <svg class="contact-icon" viewBox="0 0 20 20" aria-hidden="true">
          <circle cx="10" cy="10" r="10" fill="var(--accent-orange)"/>
          <path d="M5.5 8.5c0-2 2-3 4.5-3s4.5 1 4.5 3l-2 .5-.5-1.5h-4l-.5 1.5z M7 10h6l1 4H6z" fill="#fff"/>
        </svg>
        <span>208 367 4120</span>
      </li>
      <li class="contact-item">
        <svg class="contact-icon" viewBox="0 0 20 20" aria-hidden="true">
          <circle cx="10" cy="10" r="10" fill="var(--accent-orange)"/>
          <rect x="5" y="6.5" width="10" height="7" fill="none" stroke="#fff" stroke-width="1.3"/>
          <path d="M5 6.5l5 4 5-4" fill="none" stroke="#fff" stroke-width="1.3"/>
        </svg>
        <span>MarcusTilleySCB@mailbox-example.com</span>
      </li>
      <li class="contact-item">
        <svg class="contact-icon" viewBox="0 0 20 20" aria-hidden="true">
          <circle cx="10" cy="10" r="10" fill="var(--accent-orange)"/>
          <circle cx="10" cy="10" r="5" fill="none" stroke="#fff" stroke-width="1.3"/>
          <path d="M5 10h10M10 5c-2 3-2 7 0 10M10 5c2 3 2 7 0 10" fill="none" stroke="#fff" stroke-width="1"/>
        </svg>
        <span>Stonefieldcustombuilders-example.com</span>
      </li>
    </ul>
  </section>

  <section class="card card-back">
    <div class="back-surface" role="img" aria-label="Embossed repeating company pattern on dark brown card stock"></div>
    <p class="back-name">Stonefield Custom Builders</p>
  </section>

</main>
</body>
</html>
```